Brightmoor Surface Index

I have a current web site that it looking quite aged and it needs a new lease of life. This is a Graffiti Management Website so is all about data processing and management of information. I want a html 5 view on any platform design. clean crisp and new. I have provided some screen shots of my current site.

Target Market(s)

The Target Market will be local government. most users will not be heavy pc users

Industry/Entity Type

Management

Font styles to use
Sans Serif
Other font styles liked:
• web font like calibri

Colors

Designer to choose colors to be used in the design.

Requirements
Must have
• Must have menus similar to attachments

```html
<!DOCTYPE html>
<html lang="en">
<head>
<meta charset="utf-8">
<title>Brightmoor Surface Index</title>
<link href="https://fonts.googleapis.com/css2?family=Open+Sans:wght@400;600;700&family=PT+Serif:wght@700&display=swap" rel="stylesheet">
<style>
:root{
  --red:#ee3a23;
  --red-dark:#d8311c;
  --ink:#111;
  --text:#333;
  --muted:#777;
  --panel:#f4f4f4;
  --panel-2:#f6f6f6;
  --footer:#222;
  --white:#fff;
}
*{margin:0;padding:0;box-sizing:border-box}
html,body{width:1200px;height:2396px;overflow:hidden}
body{font-family:"Open Sans",Arial,sans-serif;color:var(--text);background:var(--white);position:relative}

/* header */
.site-header{height:112px;position:relative}
.brand{position:absolute;left:68px;top:18px}
.brand-name{font-family:"Open Sans",Arial,sans-serif;font-weight:700;color:var(--red);font-size:46px;line-height:46px;letter-spacing:1px}
.brand-tag{font-size:11px;font-weight:700;color:var(--ink);margin-top:4px;letter-spacing:.2px}
.account-links{position:absolute;right:64px;top:14px;font-size:12px;color:var(--muted)}
.main-nav{position:absolute;right:62px;top:56px;display:flex;gap:34px}
.main-nav a{font-size:14px;font-weight:700;color:var(--ink);text-decoration:none;padding-bottom:4px}
.main-nav a.active{color:var(--red);border-bottom:2px solid var(--red);font-weight:600}

/* hero */
.hero{position:relative;height:428px}
.hero-photo{position:absolute;inset:0;background:linear-gradient(180deg,#6b6a66 0%,#8d8a83 30%,#a9aba8 48%,#5d6a70 62%,#3f4b4d 100%)}
.hero-card{position:absolute;left:68px;top:110px;width:436px;height:246px;background:rgba(235,235,235,.55);padding:22px 24px}
.hero-card h1{font-family:"PT Serif",Georgia,serif;font-weight:700;font-size:28px;line-height:38px;color:#111;text-transform:uppercase}
.hero-card p{margin-top:14px;font-size:14px;line-height:21px;color:#fff}
.btn{display:inline-block;background:var(--red);color:#fff;font-size:14px;text-transform:uppercase;padding:3px 13px;text-decoration:none}
.hero-card .btn{margin-top:16px}
.slide-arrow{position:absolute;width:20px;height:20px;background:#fff;display:flex;align-items:center;justify-content:center}
.hero .slide-arrow{top:196px}
.slide-arrow.prev{left:20px}
.slide-arrow.next{right:22px}

/* welcome */
.welcome{height:312px;text-align:center;padding-top:54px}
.section-title{font-size:22px;font-weight:400;color:var(--ink);text-transform:uppercase}
.welcome .lead{font-size:17px;color:var(--ink);margin-top:22px}
.welcome p.copy{font-size:13px;color:var(--text);margin-top:20px}

/* products */
.products{height:426px;background:var(--panel);position:relative;text-align:center;padding-top:24px}
.product-grid{display:flex;position:absolute;left:68px;top:96px;gap:0}
.product{width:410px;text-align:left}
.product h3{font-size:17px;font-weight:400;color:var(--ink)}
.product-photo{width:224px;height:110px;margin-top:24px;display:flex;align-items:center;justify-content:center}
.product p{font-size:12.5px;line-height:20px;color:#222;margin-top:22px;width:282px}
.products .slide-arrow{top:196px;background:var(--red)}

/* benefits */
.benefits{height:500px;background:var(--red);position:relative;color:#fff;text-align:center;padding-top:28px}
.benefits .section-title{color:#fff}
.benefit{position:absolute;text-align:left;width:460px}
.benefit svg{position:absolute;left:0;top:0}
.benefit h3{margin-left:66px;font-size:19px;font-weight:400;text-transform:uppercase}
.benefit p{margin-left:66px;font-size:13px;line-height:24px;margin-top:6px}
.divider-v{position:absolute;left:597px;width:1px;background:rgba(255,255,255,.7)}
.divider-h{position:absolute;top:274px;height:1px;background:rgba(255,255,255,.7)}

/* legislation */
.legislation{height:422px;background:var(--panel-2);position:relative;text-align:center;padding-top:62px}
.law{position:absolute;top:142px;width:538px;height:222px;border:1px solid var(--red);background:#fff;text-align:left;padding:16px 16px}
.law h3{font-size:17px;font-weight:400;color:var(--ink)}
.law p{font-size:12.5px;line-height:21px;color:var(--muted);margin-top:26px}
.law .btn{position:absolute;left:50%;transform:translateX(-50%);bottom:16px}

/* footer */
.site-footer{height:180px;background:var(--footer);color:#fff;position:relative;text-align:center;padding-top:28px}
.site-footer h2{font-size:22px;font-weight:400;text-transform:uppercase}
.contact{position:absolute;top:82px;display:flex;gap:24px;text-align:left;font-size:13px;line-height:24px}
.copyright{height:16px;font-size:11px;text-align:center;color:#111;line-height:18px}
</style>
</head>
<body>

<header class="site-header">
  <div class="brand">
    <div class="brand-name">BSI</div>
    <div class="brand-tag">BRIGHTMOOR SURFACE INDEX</div>
  </div>
  <div class="account-links">Log In | Demo Log In</div>
  <nav class="main-nav">
    <a class="active" href="#">HOME</a>
    <a href="#">PRODUCTS</a>
    <a href="#">REPORTS</a>
    <a href="#">BENEFITS</a>
    <a href="#">LEGISLATION</a>
    <a href="#">CONTACT US</a>
  </nav>
</header>

<section class="hero">
  <div class="hero-photo" role="img" aria-label="Street with a large painted waterfall artwork on the road surface"></div>
  <div class="hero-card">
    <h1>Helping you clean up<br>your community</h1>
    <p>BSI allows you to Register, Track, Report and Archive Graffiti jobs with Photographic Records.</p>
    <a class="btn" href="#">View more</a>
  </div>
  <span class="slide-arrow prev"><svg width="10" height="12"><path d="M8 1 2 6l6 5z" fill="#111"/></svg></span>
  <span class="slide-arrow next"><svg width="10" height="12"><path d="M2 1l6 5-6 5z" fill="#111"/></svg></span>
</section>

<section class="welcome">
  <h2 class="section-title">Welcome to BSI</h2>
  <p class="lead">BSI is an Online Database System to Manage Graffiti in your area or Your Properties</p>
  <p class="copy">BSI records both Estimated and Actual hours and costs for each job, enabling you to track the effectiveness of Anti Graffiti policy.</p>
  <p class="copy">BSI has a Statistical and Comparison Reporting Systems to allow its subscribers to graphically report and compare their Graffiti Data.</p>
  <p class="copy">BSI allows sharing of Critical Graffiti Tag and Photographic Data between its subscribers, assisting with tracking down Serial Graffiti Offenders.</p>
</section>

<section class="products">
  <h2 class="section-title">Our products</h2>
  <div class="product-grid">
    <div class="product">
      <h3>Graffiti Register</h3>
      <div class="product-photo" role="img" aria-label="Colourful painted graffiti mural" style="background:linear-gradient(120deg,#2a6fb0,#d9482b 50%,#f0b03a)"></div>
      <p>BSI provides a National Register of Vandalism and Graffiti. Subscribers to the BSI Database can Add, Change, Report on and Archive their own Graffiti Jobs.</p>
    </div>
    <div class="product">
      <h3>Graffiti Photos</h3>
      <div class="product-photo" role="img" aria-label="Graffiti wall photo with a picture icon" style="background:linear-gradient(120deg,#3a3f55,#8a4a5c 55%,#2d2d33)">
        <svg width="34" height="28" viewBox="0 0 34 28"><rect x="1" y="1" width="32" height="26" rx="3" fill="none" stroke="#fff" stroke-width="2"/><path d="M5 23l8-9 6 6 4-4 6 7z" fill="#fff"/><circle cx="24" cy="8" r="3" fill="#fff"/></svg>
      </div>
      <p>BSI allows its subscribers to add Digital Photographs to the Graffiti Jobs. Cleaner Photographs can also be Added as a record of Job Completion.</p>
    </div>
    <div class="product">
      <h3>Graffiti Archive</h3>
      <div class="product-photo" role="img" aria-label="Dark graffiti-covered alley with an archive icon" style="background:linear-gradient(120deg,#2b2b2b,#555 50%,#333)">
        <svg width="32" height="28" viewBox="0 0 32 28"><rect x="1" y="1" width="30" height="26" rx="2" fill="#fff"/><rect x="5" y="6" width="22" height="2" fill="#333"/><rect x="5" y="11" width="22" height="2" fill="#333"/><path d="M1 16h9l2 4h8l2-4h9" fill="none" stroke="#333" stroke-width="2"/></svg>
      </div>
      <p>BSI will hold secure the commercial and sensitive details of your Graffiti. However the statistical and photographic records will be shared between all subscribers.</p>
    </div>
  </div>
  <span class="slide-arrow prev"><svg width="10" height="12"><path d="M8 1 2 6l6 5z" fill="#fff"/></svg></span>
  <span class="slide-arrow next"><svg width="10" height="12"><path d="M2 1l6 5-6 5z" fill="#fff"/></svg></span>
</section>

<section class="benefits">
  <h2 class="section-title">Our benefits</h2>
  <div class="divider-v" style="top:88px;height:150px"></div>
  <div class="divider-v" style="top:300px;height:170px"></div>
  <div class="divider-h" style="left:74px;width:496px"></div>
  <div class="divider-h" style="left:624px;width:500px"></div>

  <div class="benefit" style="left:80px;top:114px">
    <svg width="46" height="40" viewBox="0 0 46 40"><rect x="4" y="10" width="32" height="20" transform="rotate(-20 20 20)" fill="#fff"/><circle cx="20" cy="20" r="5" fill="var(--red)"/><rect x="30" y="18" width="12" height="16" fill="#fff"/></svg>
    <h3>Cost effective</h3>
    <p>BSI allows you to track the cost and effectiveness of your Graffiti Removal. Compare the estimates &amp; actual costs for External Contractors against inhouse removal.</p>
  </div>
  <div class="benefit" style="left:656px;top:114px">
    <svg width="40" height="40" viewBox="0 0 40 40"><rect x="6" y="2" width="28" height="20" rx="2" fill="#fff"/><rect x="2" y="14" width="30" height="22" rx="2" fill="#fff" stroke="var(--red)" stroke-width="2"/><rect x="2" y="19" width="30" height="4" fill="var(--red)"/></svg>
    <h3>Photographic records</h3>
    <p>Store any photographic records of New, Existing and Completed Graffiti Jobs. Archive all competed works including photos of "cleaned" areas.</p>
  </div>
  <div class="benefit" style="left:80px;top:308px">
    <svg width="44" height="44" viewBox="0 0 44 44"><circle cx="12" cy="6" r="5" fill="#fff"/><rect x="6" y="13" width="12" height="16" fill="#fff"/><rect x="7" y="29" width="4" height="13" fill="#fff"/><rect x="13" y="29" width="4" height="13" fill="#fff"/><circle cx="32" cy="6" r="5" fill="#fff"/><rect x="26" y="13" width="12" height="16" fill="#fff"/><rect x="27" y="29" width="4" height="13" fill="#fff"/><rect x="33" y="29" width="4" height="13" fill="#fff"/></svg>
    <h3>Assist prosecution</h3>
    <p>BSI can assist with the possible prosecution of offenders with records of previous tags inside your local area as well as any other subscribers tags. This will effectively show the extent of the offenders activities.</p>
  </div>
  <div class="benefit" style="left:656px;top:308px;width:500px">
    <svg width="36" height="42" viewBox="0 0 36 42"><path d="M9 18v-6a9 9 0 0 1 18 0v6" fill="none" stroke="#fff" stroke-width="4"/><rect x="4" y="18" width="28" height="22" rx="3" fill="#fff"/><rect x="16" y="24" width="4" height="9" fill="var(--red)"/></svg>
    <h3>Access and security</h3>
    <p>You can access your data from any PC around the world connected to the Internet. You can give access to your trusted contractors to update your data for you. You can setup personalized access with an administrators account detailing the access of all of your staff logins limiting view, add and edit levels.</p>
  </div>
</section>

<section class="legislation">
  <h2 class="section-title">Legislation</h2>
  <article class="law" style="left:48px">
    <h3>NSW Local Government Legislation Regarding Graffiti Removal</h3>
    <p>To provide the legal framework for an effective, efficient, environmentally responsible and open system of local government in New South Wales, to encourage and assist the effective participation of local communities in the affairs of local government, arole in the management, improvement and development of the resources of their areas.</p>
    <a class="btn" href="#">View more</a>
  </article>
  <article class="law" style="left:614px">
    <h3 style="margin-top:6px">NSW Local Government Graffiti Ammendment ACT 2002</h3>
    <p>The Local Government Act 1993 (the Act), has been amended by the Local Government Amendment (Graffiti) Amendment Act 2002, to enable councils to remove graffiti from property without the prior consent of the owner/ occupier where it is visible and accessible from a public place.</p>
    <a class="btn" href="#">View more</a>
  </article>
</section>

<footer class="site-footer">
  <h2>Just in case you need any help</h2>
  <div class="contact" style="left:56px">
    <svg width="26" height="24" viewBox="0 0 26 24"><path d="M13 1 1 12h4v11h6v-7h4v7h6V12h4z" fill="#fff"/></svg>
    <div>Brightmoor Surface Index<br>PO Box 418, Kelmarsh, NSW 2291</div>
  </div>
  <div class="contact" style="left:514px">
    <svg width="28" height="24" viewBox="0 0 28 24"><path d="M2 8c0-4 24-4 24 0v3h-6V8H8v3H2z" fill="#fff"/><rect x="5" y="12" width="18" height="10" rx="2" fill="#fff"/><circle cx="14" cy="17" r="3" fill="#222"/></svg>
    <div>(02) 9000 4417</div>
  </div>
  <div class="contact" style="left:888px">
    <svg width="28" height="22" viewBox="0 0 28 22"><rect x="1" y="1" width="26" height="20" fill="none" stroke="#fff" stroke-width="2"/><path d="M1 1l13 11L27 1" fill="none" stroke="#fff" stroke-width="2"/></svg>
    <div>enquiries@brightmoorsi.com.au<br>support@brightmoorsi.com.au</div>
  </div>
</footer>
<div class="copyright">copyright 2014 BSI all rights reserved</div>

</body>
</html>
```